Packaging and Insert Design for New Cocktail/Bar Set

We are launching a new product under our brand, Shakerline Guild, and require a design for the product packaging (2 packages - an inner cylinder tube and an outer box), as well as an insert.

(Note for reference - "mixology" is the art of cocktail making).

Our product is a cocktail set which will be sold on the USA Vendora site.

Our logo has already been designed - please refer to the attached files. I've attached various vector files of our logo.

The cocktail set will be packaged in a cylinder tube box.
Please see uploaded files for an image of the cylinder, as well as dimensions.
Dimensions are 37.68cm x 28cm (when the print design is laid flat).
The physical tube will be 28cm high and have a diameter of 12cm.
See uploaded file 'Dimensions - Cylinder Box' for details.

The cylinder box will be enclosed in an outer white box for protection. The outer white box will be a very basic box (i.e. not high quality) we are using just to make storage of individual units easier (and to protect the cylinder tube). It is unlikely that the outer box will be retained by the buyer. It will have a very clean, simple design. It will have our logo on the front and a barcode on the back (at the bottom).
Dimensions of the outer box are 28.5cm high and 12.5cm wide (tall and rectangular in shape).
See uploaded file 'Dimensions - White Outer Box & Paper Card' for details.

So to confirm we have 2 packages - the internal cylinder tube will have full branding, and this will then be placed in the white outer box with a simple design (logo only plus barcode at the back).

We also require a small insert to be designed (9.1cm x 5.5cm). We will include the insert in the package. The insert will have our logo and will provide the buyer with our contact details. The buyer will register their email address with us, in order to quality for warranty and a free e-book.

We need to finalise the content for the product insert, as well as the additional information to be printed on the cylinder tube.

In terms of design for the inner cylinder tube, we are leaning towards a more simple design, with our logo displayed on the front of the box.
We are open to ideas/suggestions though.

We have also uploaded an image of the cocktail set components which will form part of the set.
Updates

Target Market(s)

Our target market will be cocktail making enthusiasts/hobbyists and professionals. This includes people who would like to but a cocktail set to use at home, as well as professional bartenders.

Industry/Entity Type

Product

Colors

Designer to choose colors to be used in the design.

Requirements
Must have
• Preference is for a clean, professional looking design.
• Internal cylinder tube - full branding, incorporating logo on the front. Possibly also either a slogan e.g. "The Art of Cocktail Making' or details of the product e.g. "Cocktail Making Set' or similar.
• Outer white box - very simple design with logo to be displayed on the front of the packaging.
Should not have
• The design should not be too busy/complex. Not too much going on.

```html
<!DOCTYPE html>
<html lang="en">
<head>
<meta charset="utf-8">
<title>Shakerline Guild – Cocktail Set Tube Wrap</title>
<link rel="stylesheet" href="https://fonts.googleapis.com/css2?family=Questrial&display=swap">
<style>
  :root {
    --page-bg: #f1f1f1;
    --panel-light: #e7e7e7;
    --panel-dark: #000000;
    --ink-light: #ffffff;
    --ink-dark: #111111;
    --divider: #b5b5b5;
  }
  html, body {
    margin: 0;
    width: 1200px;
    height: 1199px;
    overflow: hidden;
    background: var(--page-bg);
  }
  .tube-wrap {
    position: absolute;
    left: 136px;
    top: 254px;
    width: 928px;
    height: 690px;
    display: block;
  }
  .wrap-text { font-family: "Questrial", sans-serif; }
  .brand-name { fill: var(--ink-light); letter-spacing: 6px; }
  .content-title { fill: var(--ink-light); font-size: 17px; }
  .content-list { fill: var(--ink-light); font-size: 11.5px; }
  .product-title { fill: var(--ink-light); font-size: 43px; }
  .tagline { fill: var(--ink-dark); font-size: 20px; }
  .tool-strip { fill: #5a5a5a; }
</style>
</head>
<body>
<svg class="tube-wrap" viewBox="0 0 850 632" xmlns="http://www.w3.org/2000/svg">
  <rect class="panel-light" x="0" y="0" width="850" height="632" fill="var(--panel-light)"/>
  <polygon class="panel-dark" fill="var(--panel-dark)"
    points="0,200 350,0 603,0 850,197 850,632 603,432 250,632 0,632"/>
  <line class="seam" x1="603" y1="432" x2="603" y2="632" stroke="var(--divider)" stroke-width="1"/>

  <g class="wrap-text">
    <text class="brand-name" x="425" y="160" text-anchor="middle" font-size="30">SHAKERLINE</text>
    <text class="brand-name" x="425" y="188" text-anchor="middle" font-size="14">GUILD</text>

    <text class="content-title" transform="translate(128,352) rotate(90)">Content</text>
    <rect class="tool-strip" x="86" y="302" width="34" height="183" rx="3"
      role="img" aria-label="Row of small line icons of the cocktail tools in the set"/>
    <text class="content-list" transform="translate(57,229) rotate(90)">content 1 - content 2 - content 3 - content 4</text>
    <text class="content-list" transform="translate(42,272) rotate(90)">content 5 - content 16 - content 7</text>

    <text class="product-title" transform="translate(298,572) rotate(-29.5)">Cocktail Set</text>

    <text class="tagline" x="580" y="575" text-anchor="end">Professionals</text>
    <text class="tagline" x="580" y="601" text-anchor="end">Tools</text>
  </g>
</svg>
</body>
</html>
```